Custom Made Digital Jukebox sales and rental website

I need a design for a Custom Made Digital Jukebox sales and rental services website. Domain name is quelitrune.com. Exisiting customer shall have a section to register, login/logout, my account, support. All other visitor shall have at least the following options or menu avaialble: Home, FAQ, Services, Products, and Contact us. I have attached a high level requirements pdf file. Please don't be limited by high level requirements file attached, your idea may be better than what I specified. My products are designed base on customer requirements. Common parts are: Bill and Coin Acceptors, Touchscreen or keypad. All of them are wall mount.

Target Market(s)

Custom made digital Jukebox for Home and Commercial use

Industry/Entity Type

Digital

Number of Pages Required

1 page

Requirements
Must have
• PSD required.
Nice to have
• HTML code and CSS Stylesheet
• Logo for QueliTrune
• Inner Pages
Should not have
• Copyright material from related websites, previously developed or any other.

```html
<!DOCTYPE html>
<html lang="en">
<head>
<meta charset="utf-8">
<title>QueliTrune — Digital Jukebox Sales &amp; Rental</title>
<link rel="stylesheet" href="https://fonts.googleapis.com/css2?family=Raleway:wght@400;500&family=Open+Sans:wght@400;600&display=swap">
<style>
  :root{
    --red:#c9260c;
    --red-dark:#9c1a06;
    --red-light:#e0391a;
    --orange:#f0621a;
    --ink:#1d1d1d;
    --text:#555;
    --hero-top:#2a2a2a;
    --hero-bottom:#070707;
    --footer-top:#f2f2f2;
    --footer-bottom:#e6e6e6;
    --social:#2b6fb5;
  }
  *{margin:0;padding:0;box-sizing:border-box}
  html,body{width:1012px;height:1200px;overflow:hidden;background:#fff}
  body{position:relative;font-family:"Open Sans",Arial,sans-serif;color:var(--text)}

  .site-header{position:absolute;left:0;top:0;width:1012px;height:79px}
  .brand{position:absolute;left:151px;top:26px;font-family:"Raleway",Arial,sans-serif;font-size:26px;font-weight:500;color:var(--ink);letter-spacing:.2px}
  .account-links{position:absolute;left:696px;top:11px;font-size:10.5px;color:#666;word-spacing:2px}
  .account-links span{margin:0 7px;color:#777}

  .main-nav{position:absolute;left:0;top:79px;width:1012px;height:40px;background:linear-gradient(#d93517,var(--red) 55%,#b41f08);border-top:1px solid #e14a2c}
  .main-nav ul{list-style:none;position:absolute;left:149px;top:0;display:flex;height:40px}
  .main-nav li{height:40px;line-height:40px;color:#fff;font-size:13px;text-align:center;border-right:1px solid rgba(255,255,255,.22)}
  .main-nav li.active{background:linear-gradient(#a41b06,#8e1604)}
  .main-nav li:last-child{border-right:none}

  .hero{position:absolute;left:0;top:119px;width:1012px;height:376px;background:linear-gradient(var(--hero-top),#161616 60%,var(--hero-bottom))}
  .hero-title{position:absolute;left:152px;top:110px;font-family:"Raleway",Arial,sans-serif;font-weight:400;font-size:27px;color:#f3f3f3;line-height:1.2}
  .hero-sub{position:absolute;left:152px;top:141px;font-family:"Raleway",Arial,sans-serif;font-weight:400;font-size:32px;color:var(--orange);line-height:1.2}
  .hero-text{position:absolute;left:153px;top:187px;width:320px;font-size:9px;line-height:15px;color:#a8a8a8}
  .slider-dots{position:absolute;left:153px;top:227px;display:flex;gap:3px}
  .slider-dots i{width:9px;height:9px;border-radius:50%;background:#6a6a6a}
  .hero-visual{position:absolute;left:560px;top:0;width:300px;height:376px;background:radial-gradient(ellipse at 50% 50%,#b8621e 0%,#6e3214 45%,rgba(20,12,8,0) 85%)}

  .features{position:absolute;left:150px;top:516px;width:712px;height:234px}
  .feature{position:absolute;top:0;width:231px}
  .feature-img{width:231px;height:120px;border-bottom:3px solid var(--orange)}
  .feature h2{font-family:"Raleway",Arial,sans-serif;font-weight:400;font-size:17px;color:#2a2a2a;margin:12px 0 4px}
  .feature p{font-size:8.3px;line-height:15.2px;color:#6d6d6d;padding-left:1px}
  .btn{display:inline-block;margin:10px 0 0 2px;width:82px;height:25px;line-height:25px;text-align:center;font-size:9.5px;color:#fff;background:linear-gradient(var(--red-light),var(--red-dark));border-radius:2px}

  .divider{position:absolute;left:158px;top:779px;width:690px;height:5px}

  .section-title{position:absolute;left:150px;top:810px;font-family:"Raleway",Arial,sans-serif;font-weight:400;font-size:18px;color:var(--red)}
  .product{position:absolute;top:846px;width:173px;height:211px;border:1px solid #d3d3d3;text-align:center}
  .product-img{margin:14px auto 0;width:110px;height:114px}
  .product h3{font-family:"Raleway",Arial,sans-serif;font-weight:500;font-size:12.5px;color:#222;margin-top:22px}
  .product p{font-size:8px;line-height:13.5px;color:#777;margin-top:3px}

  .site-footer{position:absolute;left:0;top:1103px;width:1012px;height:97px;background:linear-gradient(var(--footer-top),var(--footer-bottom));border-top:1px solid #d8d8d8}
  .footer-nav{position:absolute;left:155px;top:24px;display:flex;gap:30px;font-family:"Raleway",Arial,sans-serif;font-size:11.5px;color:#333}
  .copyright{position:absolute;left:155px;top:49px;font-size:8px;color:#555}
  .social{position:absolute;left:798px;top:26px;display:flex;gap:9px}
  .social i{width:14px;height:14px;border-radius:50%;background:var(--social)}
</style>
</head>
<body>
  <header class="site-header">
    <div class="brand">QueliTrune</div>
    <div class="account-links">Login<span>|</span>My Account<span>|</span>Support</div>
  </header>

  <nav class="main-nav">
    <ul>
      <li class="active" style="width:118px">HOME</li>
      <li style="width:94px">FAQ</li>
      <li style="width:129px">SERVICES</li>
      <li style="width:139px">PRODUCTS</li>
      <li style="width:114px">CONTACT US</li>
    </ul>
  </nav>

  <section class="hero">
    <h1 class="hero-title">Praesent elementum elit</h1>
    <div class="hero-sub">Digital Jukebox</div>
    <p class="hero-text">Aculis ipsum dui aliquet felis at cursus magna nisl nec elit Praesent elementum elit at tellus nec ultricies sit amet porttitor</p>
    <div class="slider-dots"><i></i><i></i><i></i><i></i></div>
    <div class="hero-visual" role="img" aria-label="Photo of a glowing classic jukebox on a dark background"></div>
  </section>

  <section class="features">
    <article class="feature" style="left:0">
      <div class="feature-img" role="img" aria-label="Photo of a person beside a jukebox" style="background:linear-gradient(100deg,#b98a6a,#d9c3ae 45%,#a89a8f)"></div>
      <h2>About Digital Juke box</h2>
      <p>Morbi ornare gravida elit Integer congue augue et malesu iaculis ipsum dui aliquet felis at cursus magna nisl nec elit Praesent elementum elit at tellus nec ultricies</p>
      <span class="btn">READ MORE</span>
    </article>
    <article class="feature" style="left:240px">
      <div class="feature-img" role="img" aria-label="Photo of a jukebox lit green in the dark" style="background:radial-gradient(ellipse at 50% 40%,#6f9a5e,#34432f 45%,#050505 80%)"></div>
      <h2>Services Provides</h2>
      <p>Morbi ornare gravida elit Integer congue augue et malesu iaculis ipsum dui aliquet felis at cursus magna nisl nec elit Praesent elementum elit at tellus nec ultricies</p>
      <span class="btn">READ MORE</span>
    </article>
    <article class="feature" style="left:481px">
      <div class="feature-img" role="img" aria-label="Close-up photo of jukebox lights" style="background:linear-gradient(110deg,#7a1408,#c8402a 40%,#d88a48 70%,#6a2a10)"></div>
      <h2>Buy or Rent Jukebox</h2>
      <p>Morbi ornare gravida elit Integer congue augue et malesu iaculis ipsum dui aliquet felis at cursus magna nisl nec elit Praesent elementum elit at tellus nec ultricies</p>
      <span class="btn">BUY NOW</span>
    </article>
  </section>

  <svg class="divider" viewBox="0 0 690 5" aria-hidden="true">
    <line x1="0" y1="2.5" x2="338" y2="2.5" stroke="#e4e4e4" stroke-width="2"/>
    <rect x="343" y="0.5" width="4" height="4" fill="none" stroke="#cfcfcf" stroke-width="0.8"/>
    <rect x="347" y="0.5" width="4" height="4" fill="none" stroke="#cfcfcf" stroke-width="0.8"/>
    <line x1="356" y1="2.5" x2="690" y2="2.5" stroke="#e4e4e4" stroke-width="2"/>
  </svg>

  <h2 class="section-title">Featured Juke Boxes</h2>

  <article class="product" style="left:150px">
    <div class="product-img" role="img" aria-label="Product photo of a wooden jukebox" style="background:linear-gradient(#f4ece6,#d9b7a0)"></div>
    <h3>Juke Box Tittle</h3>
    <p>Morbi ornare gravida elit Integer<br>congue augue et malesu iacu</p>
  </article>
  <article class="product" style="left:330px">
    <div class="product-img" role="img" aria-label="Product photo of a classic yellow jukebox" style="background:linear-gradient(#f6efe2,#e2c48a)"></div>
    <h3>Juke Box Tittle</h3>
    <p>Morbi ornare gravida elit Integer<br>congue augue et malesu iacu</p>
  </article>
  <article class="product" style="left:509px">
    <div class="product-img" role="img" aria-label="Product photo of a blue-lit jukebox" style="background:linear-gradient(#eceef4,#aab6d6)"></div>
    <h3>Juke Box Tittle</h3>
    <p>Morbi ornare gravida elit Integer<br>congue augue et malesu iacu</p>
  </article>
  <article class="product" style="left:689px">
    <div class="product-img" role="img" aria-label="Product photo of a touchscreen jukebox" style="background:linear-gradient(#eef2ec,#c6cfa8)"></div>
    <h3>Juke Box Tittle</h3>
    <p>Morbi ornare gravida elit Integer<br>congue augue et malesu iacu</p>
  </article>

  <footer class="site-footer">
    <nav class="footer-nav"><span>Home</span><span>FAQ</span><span>Services</span><span>Products</span><span>Contact Us</span></nav>
    <div class="copyright">© 2015 Company Name &nbsp;All right reserved &nbsp;Term of Use</div>
    <div class="social" aria-label="Social links"><i></i><i></i><i></i></div>
  </footer>
</body>
</html>
```